Flyer-Design für Internethandel auf ausgewählten Marktplätzen
Zielgruppe
Internethandel auf Marktplätzen wie: Verkano, Lumo, Fiska.de, Brix.de
Eigene Webseite: www.talbrunn-laden.de
So ganz festgelegt habe ich mch noch nicht was ich alles im Sortiment haben möchte.
Im Moment besteht der Hauptteil aus Pflaster verschiedenster Sorten, aus verschiedenen Klebebandsorten und aus Werkzeugen wie Cuttermesser und passende Klingen.
Aufgabenstellung
Ich möchte (mit den Farben des Logos ?) einen Flyer, um Käufer darum zu bitten eine bewertung für mich abzugeben.
Soetwas wie: wir sind stets bemüht unsere Service-Leistungen zu verbessern und freuen uns, wenn Sie diese mit einer positven Bewertung honorieren. Siehe angehängtes Bild, das habe ich heute von einem anderen verkäufer bekommen.
Sehr gerne auch einen anderen passenden Text.
Was ich auch gerne hätte, wäre der Hinweis auf unsere Webseite www.talbrunn-laden.de
Dort bieten wir auch Staffelpreise an und Käufer können dadurch sparen wenn Sie mehr kaufen.
Ich habe mal zwei Bilder von Klebebänder mit angehängt. Eventuell können Sie ja auf unserer Internetseite ein Passendes Bild von Klebebandrollen, Pflaster oder Arbeitsschutzmaterial kopieren.
Es ist aber kein muss ein Bild mit ein zu setzen.
Bedruckt werden sollten beide seiten. Größe: Ca. Postkartengröße?!

```html
<!DOCTYPE html>
<html lang="de">
<head>
<meta charset="utf-8">
<title>Talbrunn Laden – Bewertungs-Flyer</title>
<link rel="stylesheet" href="https://fonts.googleapis.com/css2?family=Kumbh+Sans:wght@400;700&family=Caveat:wght@600&display=swap">
<style>
  :root {
    --page: #f3f3f3;
    --front-top: #d9d9d9;
    --front-bottom: #efefef;
    --text: #555555;
    --heading: #4a4a4a;
    --green: #8fab2e;
    --blue: #1d4a73;
    --yellow: #f7d100;
    --brand-green: #4cb848;
    --icon-green: #22c51e;
    --white: #ffffff;
    --star: #f7d51a;
  }
  * { margin: 0; padding: 0; box-sizing: border-box; }
  html, body { width: 1109px; height: 1200px; overflow: hidden; }
  body {
    background: var(--page);
    font-family: "Kumbh Sans", sans-serif;
    color: var(--text);
    position: relative;
  }
  .card { position: absolute; overflow: hidden; }

  /* Front side */
  .card-front {
    left: 102px; top: 114px; width: 647px; height: 458px;
    background: linear-gradient(160deg, var(--front-top), var(--front-bottom));
  }
  .greeting {
    position: absolute; left: 92px; top: 46px;
    font-family: "Caveat", cursive; font-weight: 600;
    font-size: 34px; color: var(--heading);
  }
  .brand {
    position: absolute; display: flex; align-items: center; gap: 6px;
    font-size: 15px; font-weight: 400; color: var(--heading); white-space: nowrap;
  }
  .brand-dot { width: 10px; height: 10px; border-radius: 50%; background: var(--brand-green); }
  .card-front .brand { left: 490px; top: 68px; }
  .intro, .request {
    position: absolute; left: 92px; font-size: 12.5px; line-height: 20.2px;
  }
  .intro { top: 104px; }
  .request { top: 266px; }
  .stars { position: absolute; left: 92px; top: 196px; display: flex; gap: 8px; }
  .stars svg { width: 40px; height: 40px; }
  .photo-hands {
    position: absolute; left: 84px; top: 312px; width: 476px; height: 135px;
    background: linear-gradient(180deg, rgba(233,233,233,0) 0%, #d9b39a 55%, #c89a7e 100%);
    border-radius: 40px 40px 0 0;
  }
  .tricolor { position: absolute; left: 0; bottom: 0; width: 100%; height: 11px; display: flex; }
  .tricolor span { flex: 1; }
  .tricolor .g { background: var(--green); }
  .tricolor .b { background: var(--blue); }
  .tricolor .y { background: var(--yellow); }

  /* Back side */
  .card-back {
    left: 334px; top: 630px; width: 646px; height: 455px;
    background: var(--white);
  }
  .banner {
    position: absolute; left: 4px; top: 0; width: 640px; height: 144px;
    background: linear-gradient(90deg, #eaeaea 0%, #bfc6cc 35%, #a9b3bb 55%, #e2dfd8 75%, #e9e4dc 100%);
  }
  .banner-band { position: absolute; left: 0; bottom: 0; width: 100%; height: 13px; display: flex; }
  .banner-band .g { width: 208px; background: var(--green); }
  .banner-band .b { width: 228px; background: var(--blue); }
  .banner-band .y { flex: 1; background: var(--yellow); }
  .banner-label { position: absolute; font-size: 10.5px; color: #3a3a3a; }
  .label-first-aid { left: 31px; top: 54px; }
  .label-household { left: 382px; top: 24px; }
  .label-diy { left: 350px; top: 72px; }

  .tagline {
    position: absolute; left: 47px; top: 170px;
    color: var(--brand-green); font-weight: 700; font-size: 14.5px; line-height: 23px;
  }
  .card-back .brand { left: 454px; top: 183px; }
  .benefit { position: absolute; top: 235px; width: 170px; }
  .benefit-1 { left: 41px; }
  .benefit-2 { left: 229px; }
  .benefit-3 { left: 416px; }
  .benefit-head { display: flex; gap: 10px; align-items: flex-start; }
  .benefit-icon { flex: none; width: 25px; height: 25px; }
  .benefit-title {
    font-weight: 700; font-size: 13px; line-height: 20px; color: var(--heading); padding-top: 4px;
  }
  .benefit-text { margin: 4px 0 0 6px; font-size: 12.8px; line-height: 19.8px; }
  .benefit-3 .benefit-text { margin-top: 2px; }
  .site-button {
    position: absolute; left: 403px; top: 384px; width: 186px; height: 36px;
    border-radius: 18px; background: var(--brand-green); color: var(--white);
    font-size: 12.5px; display: flex; align-items: center; justify-content: center;
  }
</style>
</head>
<body>

<section class="card card-front" aria-label="Vorderseite">
  <h1 class="greeting">Liebe Kunden,</h1>
  <div class="brand"><span class="brand-dot"></span>Talbrunn Laden</div>
  <p class="intro">
    herzlichen Dank für Ihre Bestellung und Ihr Vertrauen!<br>
    Unser Bestreben ist es, Ihnen nicht nur einwandfreie Produkte<br>
    und Leistungen anzubieten, sondern auch unseren Service stets<br>
    zu verbessern.
  </p>
  <div class="stars" aria-label="Fünf Sterne">
    <svg viewBox="0 0 24 24"><path fill="var(--star)" d="M12 1.5l3.2 6.9 7.5.9-5.5 5.2 1.4 7.5L12 18.3 5.4 22l1.4-7.5L1.3 9.3l7.5-.9z"/></svg>
    <svg viewBox="0 0 24 24"><path fill="var(--star)" d="M12 1.5l3.2 6.9 7.5.9-5.5 5.2 1.4 7.5L12 18.3 5.4 22l1.4-7.5L1.3 9.3l7.5-.9z"/></svg>
    <svg viewBox="0 0 24 24"><path fill="var(--star)" d="M12 1.5l3.2 6.9 7.5.9-5.5 5.2 1.4 7.5L12 18.3 5.4 22l1.4-7.5L1.3 9.3l7.5-.9z"/></svg>
    <svg viewBox="0 0 24 24"><path fill="var(--star)" d="M12 1.5l3.2 6.9 7.5.9-5.5 5.2 1.4 7.5L12 18.3 5.4 22l1.4-7.5L1.3 9.3l7.5-.9z"/></svg>
    <svg viewBox="0 0 24 24"><path fill="var(--star)" d="M12 1.5l3.2 6.9 7.5.9-5.5 5.2 1.4 7.5L12 18.3 5.4 22l1.4-7.5L1.3 9.3l7.5-.9z"/></svg>
  </div>
  <p class="request">
    Hierzu benötigen wir Ihr Feedack und freuen uns über<br>
    &nbsp;Ihre Bewertung – danke!
  </p>
  <div class="photo-hands" role="img" aria-label="Foto: viele erhobene Hände mit Daumen nach oben"></div>
  <div class="tricolor"><span class="g"></span><span class="b"></span><span class="y"></span></div>
</section>

<section class="card card-back" aria-label="Rückseite">
  <div class="banner" role="img" aria-label="Fotocollage: Erste-Hilfe-Koffer mit Sportlerin, Handwerker mit Bohrmaschinen und Werkzeugkasten, Paar mit Putzmitteln und Tüchern">
    <span class="banner-label label-first-aid">ERSTE HILFE</span>
    <span class="banner-label label-household">Haushaltsartikel</span>
    <span class="banner-label label-diy">Heimwerkerbedarf</span>
    <div class="banner-band"><span class="g"></span><span class="b"></span><span class="y"></span></div>
  </div>

  <h2 class="tagline">
    Ihr Online-Shop für Verbandstoffe, Wundversorgung<br>
    Haushalts- und Heimwerkerbedarf
  </h2>
  <div class="brand"><span class="brand-dot"></span>Talbrunn Laden</div>

  <div class="benefit benefit-1">
    <div class="benefit-head">
      <svg class="benefit-icon" viewBox="0 0 24 24"><circle cx="12" cy="12" r="11" fill="var(--icon-green)" stroke="#111" stroke-width="1"/><path d="M7 12.5l3.2 3.2L17 9" fill="none" stroke="#111" stroke-width="1.8" stroke-linecap="round" stroke-linejoin="round"/></svg>
      <h3 class="benefit-title">Gratis-Geschenk</h3>
    </div>
    <p class="benefit-text">Ein Einkauf bei uns lohnt<br>sich immer, denn zu den<br>unschlagbar günstigen<br>Preisen erhalten Sie bei<br>Ihrem Einkauf ab 15 € ein<br>Gratis-Geschenk.</p>
  </div>

  <div class="benefit benefit-2">
    <div class="benefit-head">
      <svg class="benefit-icon" viewBox="0 0 24 24"><circle cx="12" cy="12" r="11" fill="var(--icon-green)" stroke="#111" stroke-width="1"/><path d="M7 12.5l3.2 3.2L17 9" fill="none" stroke="#111" stroke-width="1.8" stroke-linecap="round" stroke-linejoin="round"/></svg>
      <h3 class="benefit-title">Mengenrabatte</h3>
    </div>
    <p class="benefit-text">Ab 3 Stück bekommen Sie<br>bei uns schon einen attrak-<br>tiven Mengenrabatt. Kombi-<br>nation mit gleichwertigen<br>Artikeln möglich.</p>
  </div>

  <div class="benefit benefit-3">
    <div class="benefit-head">
      <svg class="benefit-icon" viewBox="0 0 24 24"><circle cx="12" cy="12" r="11" fill="var(--icon-green)" stroke="#111" stroke-width="1"/><path d="M7 12.5l3.2 3.2L17 9" fill="none" stroke="#111" stroke-width="1.8" stroke-linecap="round" stroke-linejoin="round"/></svg>
      <h3 class="benefit-title">Sparen Sie sich die<br>Versandkosten</h3>
    </div>
    <p class="benefit-text">Ab 75 Euro Warenwert über-<br>nehmen wir die Versand-<br>kosten innerhalb Deutsch-<br>land für Sie.</p>
  </div>

  <div class="site-button">www.talbrunn-laden.de</div>
</section>

</body>
</html>
```